Tallow & Mersey Needs New Stationery / Letterhead Design

We need new stationery to match our new logo (attached). Tallow & Mersey is a 34 year old nationwide law firm located in Houston Tx. They do personal injury law and pharmaceutical litigation.

WE DO NOT NEED BUSINESS CARDS.

Attached are several different file formats of the new logo.

Reason: We will make a decision in the next couple days. Finalizing edits now. Thank you!

Target Market(s)

consumers who have been injured due to the negligence of another or by a pharmaceutical drug or defective medical device. Also co-counsel and opposing counsel (law firms0.

Industry/Entity Type

Law Firm

Requirements
Must have
• logo
• Tallow & Mersey, LLP
• 7183 Corvid Lane, Suite 1000
• Brenford, TX 75591
• Tel: (555) 408-1936
• Fax: (555) 408-2275
• www.tallowandmersey.example
• Must have colors in the logo.
• Make the font go with the logo - not necessarily the same, but something that goes well with it.

```html
<!DOCTYPE html>
<html lang="en">
<head>
<meta charset="utf-8">
<title>Tallow &amp; Mersey Letterhead</title>
<link rel="stylesheet" href="https://fonts.googleapis.com/css2?family=Lato:wght@300;400;700&display=swap">
<style>
  :root {
    --backdrop: #ececec;
    --paper: #fbfbfb;
    --ink: #1e1e1e;
    --navy: #17365c;
    --charcoal: #3b3b3d;
    --footer-text: #e9eef5;
    --signature-tone: #d9d9d9;
  }
  * { box-sizing: border-box; margin: 0; padding: 0; }
  html, body {
    width: 1200px; height: 1200px; overflow: hidden;
    background: var(--backdrop);
    font-family: "Lato", sans-serif;
    color: var(--ink);
  }
  .letterhead {
    position: absolute;
    left: 167px; top: 40px;
    width: 866px; height: 1120px;
    background: var(--paper);
    box-shadow: 0 4px 18px rgba(0,0,0,0.12);
  }
  .brand {
    position: absolute; left: 250px; top: 70px;
    display: flex; align-items: center; gap: 12px;
  }
  .brand-square { width: 26px; height: 26px; background: var(--navy); }
  .brand-name {
    font-size: 30px; font-weight: 700; color: var(--navy);
    letter-spacing: 0.5px;
  }
  .letter-date {
    position: absolute; right: 110px; top: 170px;
    font-size: 14px; letter-spacing: 0.5px;
  }
  .letter-subject {
    position: absolute; left: 95px; top: 275px;
    font-size: 15px; letter-spacing: 0.3px; text-transform: uppercase;
  }
  .letter-body {
    position: absolute; left: 95px; top: 330px; width: 640px;
    font-size: 14px; line-height: 1.62;
  }
  .letter-body p + p { margin-top: 22px; }
  .signoff {
    position: absolute; left: 540px; top: 660px; width: 200px;
  }
  .signature-mark {
    display: block; width: 170px; height: 56px;
    background: linear-gradient(90deg, var(--paper), var(--signature-tone), var(--paper));
  }
  .signature-rule { border-top: 1px solid var(--ink); width: 190px; margin-top: 2px; }
  .signer-name { font-size: 12px; letter-spacing: 1px; margin-top: 4px; }
  .signer-title { font-size: 9px; text-transform: uppercase; letter-spacing: 0.3px; }
  .footer-strip {
    position: absolute; left: 0; right: 0; bottom: 150px; height: 14px;
    background: var(--charcoal);
  }
  .footer-band {
    position: absolute; left: 0; right: 0; bottom: 0; height: 150px;
    background: var(--navy); color: var(--footer-text);
    display: flex; flex-direction: column; justify-content: center; align-items: center;
    gap: 16px;
  }
  .contact-row { display: flex; gap: 52px; font-size: 17px; font-weight: 300; }
  .contact-item { display: flex; align-items: center; gap: 12px; }
  .contact-icon {
    width: 20px; height: 20px; background: var(--charcoal);
    display: flex; align-items: center; justify-content: center;
  }
  .contact-icon svg { width: 12px; height: 12px; fill: var(--footer-text); }
  .address-line { font-size: 15px; font-weight: 300; }
</style>
</head>
<body>
  <main class="letterhead">
    <header class="brand">
      <span class="brand-square"></span>
      <span class="brand-name">Tallow &amp; Mersey</span>
    </header>

    <div class="letter-date">DATE: 14/14/14</div>
    <div class="letter-subject">Subject of Interest</div>

    <section class="letter-body">
      <p>Lorem ipsum dolor sit amet, consectetur adipiscing elit. Quisque fringilla quam quis odio auctor in egestas ante pharetra. Fusce placerat tempor turpis vel euismod. Donec metus diam, interdum nec gravida tincidunt, molestie sit amet nisl. Aliquam pharetra tempus lorem, vitae ullamcorper magna scelerisque sit amet. Quisque et porttitor dolor. Ut dapibus, turpis quis lacinia cursus, risus ante cursus risus, vel luctus erat magna a ligula. Phasellus vulputate sapien orci, sed bibendum nisl. Cras dignissim, sapien ac cursus commodo, elit magna vulputate tellus, id sagittis enim dolor nec felis. Aliquam ornare lorem ut ipsum ullamcorper commodo. Curabitur tristique rutrum erat, iaculis laoreet libero sagittis non.</p>
      <p>Ut feugiat ligula sed nisi condimentum tempus. Ut eu libero purus, luctus blandit felis. Phasellus in diam ipsum, vitae tempus odio. Nullam pellentesque mauris in ligula consectetur viverra.</p>
    </section>

    <div class="signoff">
      <span class="signature-mark" role="img" aria-label="Handwritten signature of the executive director"></span>
      <div class="signature-rule"></div>
      <div class="signer-name">Hale Corbin</div>
      <div class="signer-title">Executive Director</div>
    </div>

    <div class="footer-strip"></div>
    <footer class="footer-band">
      <div class="contact-row">
        <span class="contact-item">
          <span class="contact-icon"><svg viewBox="0 0 24 24"><path d="M6.6 10.8a15.1 15.1 0 0 0 6.6 6.6l2.2-2.2a1 1 0 0 1 1-.25 11.4 11.4 0 0 0 3.6.57 1 1 0 0 1 1 1V20a1 1 0 0 1-1 1A17 17 0 0 1 3 4a1 1 0 0 1 1-1h3.5a1 1 0 0 1 1 1c0 1.25.2 2.45.57 3.57a1 1 0 0 1-.25 1z"/></svg></span>
          (555) 408-1936
        </span>
        <span class="contact-item">
          <span class="contact-icon"><svg viewBox="0 0 24 24"><path d="M6 2h9l3 3v5H6zM3 11h18v9H3zm3 3v2h4v-2z"/></svg></span>
          (555) 408-2275
        </span>
        <span class="contact-item">
          <span class="contact-icon"><svg viewBox="0 0 24 24"><path d="M12 2a10 10 0 1 0 0 20 10 10 0 0 0 0-20zm0 2c1 1.2 1.8 3 2.1 5H9.9C10.2 7 11 5.2 12 4zM4.3 11h3.6a16 16 0 0 0 .3 2H4.5a8 8 0 0 1-.2-2zm5.6 0h4.2a14 14 0 0 1-.3 2h-3.6a14 14 0 0 1-.3-2zm6.2 0h3.6a8 8 0 0 1-.2 2h-3.7a16 16 0 0 0 .3-2zM9.9 15h4.2c-.4 2-1.1 3.8-2.1 5-1-1.2-1.7-3-2.1-5z"/></svg></span>
          www.tallowandmersey.example
        </span>
      </div>
      <div class="address-line">Tallow &amp; Mersey, LLP, 7183 Corvid Lane, Suite 1000, Brenford, TX 75591</div>
    </footer>
  </main>
</body>
</html>
```